Design some Business Cards, Stationary and facebook banner/profile picture for Brookhollow Dental Spa

We are opening a brand new dental practice called "Brookhollow Dental Spa". We offer state of the art dentistry as well as injectables etc for wrinkle reduction and lip enhancement. We have a logo which can be seen at our website brookhollowdentalspa.com.au. We would like the business cards to have room to write appointments on the back (Day/Date/Time)-probably about 3 lines (to make 3 seperate appointments) with a line underneath stating "Please give at least 24hrs notice to change or cancel appointments.". The logo need only appear on the front of the card. We want the feel to be warm and not too clinical. Colours are beige, brown and the blue/green logo. We will also require A5 and A4 letterheads, envelopes, and "with compliments" slips.

Brookhollow Dental Spa
Suite 5, 417-423 Talbeck Rd
East Varnley NSW 2250
Ph (02) 4817-6052
Email - brookhollowdentalspa@[login to view URL]
Website - [login to view URL]

```html
<!DOCTYPE html>
<html lang="en">
<head>
<meta charset="utf-8">
<title>Brookhollow Dental Spa – Business Card</title>
<link rel="stylesheet" href="https://fonts.googleapis.com/css2?family=Arimo:wght@400&display=swap">
<style>
  :root {
    --card-beige: #efc48b;
    --brand-teal: #3aa9c4;
    --name-ink: #3b3530;
    --text-ink: #262626;
  }
  html, body {
    margin: 0;
    padding: 0;
    width: 1200px;
    height: 687px;
    overflow: hidden;
    background: var(--card-beige);
  }
  .card {
    position: relative;
    width: 1200px;
    height: 687px;
    background: var(--card-beige);
    font-family: "Arimo", Arial, sans-serif;
  }
  .brand-mark {
    position: absolute;
    left: 183px;
    top: 62px;
    width: 180px;
    height: 180px;
    border-radius: 50%;
    background: var(--brand-teal);
  }
  .brand-name {
    position: absolute;
    left: 40px;
    top: 262px;
    width: 470px;
    margin: 0;
    text-align: center;
    font-weight: 400;
    color: var(--name-ink);
  }
  .brand-name .line-main {
    display: block;
    font-size: 62px;
    line-height: 72px;
    letter-spacing: 2px;
  }
  .brand-name .line-sub {
    display: block;
    font-size: 50px;
    line-height: 64px;
    letter-spacing: 6px;
  }
  .contact {
    position: absolute;
    left: 544px;
    top: 413px;
    margin: 0;
    font-style: normal;
    font-size: 28px;
    line-height: 38.7px;
    color: var(--text-ink);
  }
  .contact span { display: block; white-space: nowrap; }
  .contact .email-address { text-decoration: underline; }
</style>
</head>
<body>
  <main class="card">
    <div class="brand-mark" aria-hidden="true"></div>
    <h1 class="brand-name">
      <span class="line-main">Brookhollow</span>
      <span class="line-sub">Dental Spa</span>
    </h1>
    <address class="contact">
      <span>Suite 5, 417-423 Talbeck Rd</span>
      <span>East Varnley NSW 2250</span>
      <span>Ph (02) 4817-6052</span>
      <span>Fax (02) 4817- 6052</span>
      <span>Email - <span class="email-address" style="display:inline">brookhollowdentalspa@postmail.com</span></span>
      <span>Website - www.brookhollowdentalspa.com.au</span>
    </address>
  </main>
</body>
</html>
```